Mobile technology Business Card Design Project

We need a business card design for our company based in Sydeny Australia, that takes a company's desktop sites and creates a mobile site compatible to all mobile/smartphone devices. This allows greater ease of use and generally faster business conversion than customers using a desktop site.
Our company is called Zelvora but we refer to it as Zelvora Solutions. If this could be represented somewhere on the business card that would be great.
Am open to suggestions regarding the colours but a high tech  theme would be good.
Happy bidding!

Target Market(s)
Business owner that has a website and is reasonably savvy regarding online/mobile marketing.
Industry/Entity Type
Business
Requirements
Must have
- Business card details:
Director Peter Hawkley
Address: 4/15 Brenton rd, Kelmore. 2047
Email: tbc
Web: www.zelvora-example.com.au
The cards need to have two different names for the two directors.
Damien Ferrowe & Peter Hawkley (two separate business cards)

```html
<!DOCTYPE html>
<html lang="en">
<head>
<meta charset="utf-8">
<title>Zelvora Business Card</title>
<link rel="stylesheet" href="https://fonts.googleapis.com/css2?family=Exo+2:wght@400;500&family=Open+Sans:wght@400;600&display=swap">
<style>
  :root {
    --stage: #1f1f20;
    --card-dark: #0e0e0f;
    --card-dark-edge: #1a1a1c;
    --card-light: #f7f7f7;
    --decor-grey: #e2e2e2;
    --brand-blue: #1a9ad6;
    --brand-orange: #f39a1e;
    --ink: #1b1b1b;
    --ink-soft: #3a3a3a;
  }
  * { margin: 0; padding: 0; box-sizing: border-box; }
  html, body { width: 1200px; height: 900px; overflow: hidden; }
  body {
    background: var(--stage);
    display: flex;
    align-items: center;
    justify-content: center;
    gap: 60px;
    font-family: "Open Sans", Arial, sans-serif;
  }
  .card {
    width: 500px;
    height: 290px;
    position: relative;
    overflow: hidden;
    box-shadow: 0 14px 30px rgba(0,0,0,0.55);
  }

  /* Front */
  .card-front {
    background: radial-gradient(circle at 50% 45%, var(--card-dark-edge), var(--card-dark) 70%);
    display: flex;
    flex-direction: column;
    align-items: center;
    justify-content: center;
  }
  .front-mark {
    width: 78px; height: 78px;
    border-radius: 50%;
    background: var(--brand-blue);
    margin-bottom: 14px;
  }
  .front-name {
    font-family: "Exo 2", Arial, sans-serif;
    font-weight: 500;
    font-size: 58px;
    line-height: 1;
    letter-spacing: 2px;
    color: var(--brand-blue);
  }
  .front-tagline {
    font-size: 17px;
    color: var(--brand-orange);
    margin-top: 4px;
  }

  /* Back */
  .card-back { background: var(--card-light); }
  .back-decor {
    position: absolute;
    left: -40px; top: -60px;
    width: 420px; height: 420px;
    border-radius: 50%;
    background: radial-gradient(circle, rgba(226,226,226,0) 30%, var(--decor-grey) 55%, rgba(226,226,226,0) 72%);
  }
  .back-content {
    position: absolute;
    left: 110px; top: 48px;
  }
  .back-brand { display: flex; align-items: center; gap: 10px; }
  .back-mark {
    width: 44px; height: 44px; border-radius: 50%;
    background: var(--brand-blue);
  }
  .back-name {
    font-family: "Exo 2", Arial, sans-serif;
    font-weight: 500;
    font-size: 36px;
    line-height: 1;
    color: var(--ink);
  }
  .back-tagline {
    font-size: 13px;
    color: var(--brand-orange);
    margin: 2px 0 0 54px;
  }
  .detail {
    position: relative;
    padding-left: 14px;
    margin-left: 54px;
    color: var(--ink-soft);
  }
  .detail::before {
    content: "";
    position: absolute;
    left: 0; top: 2px; bottom: 2px;
    width: 3px;
  }
  .detail-person { margin-top: 14px; }
  .detail-person::before { background: var(--ink); }
  .detail-address { margin-top: 10px; }
  .detail-address::before { background: var(--brand-orange); }
  .detail-contact { margin-top: 10px; }
  .detail-contact::before { background: var(--brand-blue); }
  .person-name { font-size: 18px; color: var(--ink); line-height: 1.2; }
  .person-role { font-size: 11px; }
  .detail-line { font-size: 12.5px; line-height: 1.35; }
</style>
</head>
<body>
  <section class="card card-front" aria-label="Card front">
    <div class="front-mark"></div>
    <div class="front-name">Zelvora</div>
    <div class="front-tagline">Making Commerce Portable</div>
  </section>

  <section class="card card-back" aria-label="Card back">
    <div class="back-decor" role="img" aria-label="Faint large brand decoration"></div>
    <div class="back-content">
      <div class="back-brand">
        <div class="back-mark"></div>
        <div class="back-name">Zelvora</div>
      </div>
      <div class="back-tagline">Making Commerce Portable</div>

      <div class="detail detail-person">
        <div class="person-name">Damien Ferrowe</div>
        <div class="person-role">Director</div>
      </div>
      <div class="detail detail-address">
        <div class="detail-line">4/15 Brenton rd, Kelmore. 2047</div>
      </div>
      <div class="detail detail-contact">
        <div class="detail-line">DFerrowe@zelvora-example.com.au</div>
        <div class="detail-line">www.zelvora-example.com.au</div>
      </div>
    </div>
  </section>
</body>
</html>
```